Tobias Wrenfield Business Card

In addition to my name design (file uploaded), black print on white card stock, e-mail address should be presented as a typical e-mail address, i.e., underlined and in blue ink, the card should include the following information:
Professor of Aviation Technology
Accident Litigation Expert Witness
Master Certificated Flight Instructor

twrenfield@qorvanet.net
Anchorage, Alaska
(907) 518-2736

Industry/Entity Type

Business

```html
<!DOCTYPE html>
<html lang="en">
<head>
<meta charset="utf-8">
<title>Tobias Wrenfield Business Card</title>
<link rel="stylesheet" href="https://fonts.googleapis.com/css2?family=Oswald:wght@600&family=Archivo+Narrow:wght@400&display=swap">
<style>
  :root {
    --card: #ffffff;
    --ink: #111111;
    --link: #1a1aff;
  }
  html, body {
    margin: 0;
    padding: 0;
    width: 1200px;
    height: 720px;
    overflow: hidden;
    background: var(--card);
  }
  .card {
    position: relative;
    width: 1200px;
    height: 720px;
    background: var(--card);
    color: var(--ink);
    font-family: "Archivo Narrow", "Arial Narrow", sans-serif;
  }
  .name {
    position: absolute;
    left: 0;
    right: 0;
    top: 280px;
    margin: 0;
    text-align: center;
    font-family: "Oswald", "Arial Narrow", sans-serif;
    font-weight: 600;
    font-size: 60px;
    line-height: 76px;
    letter-spacing: 1px;
    text-transform: uppercase;
    color: var(--ink);
  }
  .titles {
    position: absolute;
    left: 0;
    right: 0;
    top: 430px;
    margin: 0;
    padding: 0;
    list-style: none;
    text-align: center;
    font-size: 36px;
    line-height: 44px;
    letter-spacing: 2px;
  }
  .contact {
    position: absolute;
    left: 0;
    right: 0;
    top: 592px;
    margin: 0;
    text-align: center;
    font-size: 31px;
    line-height: 40px;
    letter-spacing: 1.5px;
    white-space: nowrap;
  }
  .contact .email {
    color: var(--link);
    text-decoration: underline;
    text-decoration-thickness: 1px;
    text-underline-offset: 4px;
  }
  .contact .divider {
    margin: 0 26px;
  }
</style>
</head>
<body>
  <main class="card">
    <h1 class="name">Tobias E. Wrenfield</h1>
    <ul class="titles">
      <li>Professor of Aviation Technology</li>
      <li>Accident Litigation Expert Witness</li>
      <li>Master Certificated Flight Instructor</li>
    </ul>
    <p class="contact">
      <a class="email" href="mailto:twrenfield@qorvanet.net">twrenfield@qorvanet.net</a><span class="divider">|</span><span class="location">Anchorage, Alaska</span><span class="divider">|</span><span class="phone">(907) 518-2736</span>
    </p>
  </main>
</body>
</html>
```